IT Recruitment Agency needs PSD templates to advertise candidates on Vexora Status update

BRAMO Recruitment needs a 3-5 psd templates to advertise 'hot' and available candidates we have on our database to be placed as a stauts update on Vexora and other social media sites. The design needs to fit within standard square picture size for a Vexora status update (500x500px).
The picture needs the job title of the person, 3-5 bullet points so we can highlight the attributes of the person, and at the bottom a Call To Action and contact details. In the background we should have our logo - but mainly an engaging picture - ideally one of a business female, one of a business male and 1-2 of a professional environment (business / it related). We should be able to update the text sections in the PSD ourselves for reuse - and maybe also update the main background picture. We don't want stock pictures. Our logo is below for use - it only needs to be small and not tae up the main picture which is really about highlighting an available candidate we have. We are a IT company so think hi-tech.

Target Market(s)

Hiring managers, HR, IT Managers

Industry/Entity Type

Recruitment

Font styles to use
Sans Serif

Colors
0255a3
f78f20
ec1f27
00a990
abd036

Requirements
Must have
• Non-stock images and have a IT / buiness related theme.
Nice to have
• 3-5 psd temaples we can reuse and re-edit the text sections
Should not have
• clipart!

```html
<!DOCTYPE html>
<html lang="en">
<head>
<meta charset="utf-8">
<title>BRAMO Recruitment – Candidate Status Update</title>
<link rel="stylesheet" href="https://fonts.googleapis.com/css2?family=Arimo:wght@400;700&display=swap">
<style>
  :root {
    --navy: #143f6f;
    --navy-deep: #0f3566;
    --button-top: #2a64ab;
    --button-bottom: #123d74;
    --page: #ffffff;
    --card: #fbfbfb;
    --photo-light: #f4f4f4;
    --photo-mid: #d9d9d9;
    --text-dark: #1c1c1c;
    --text-grey: #555555;
    --divider: #9a9a9a;
    --white: #ffffff;
  }
  * { box-sizing: border-box; margin: 0; padding: 0; }
  html, body {
    width: 1200px;
    height: 806px;
    overflow: hidden;
    background: var(--page);
    font-family: "Arimo", Arial, sans-serif;
  }
  .post {
    position: absolute;
    left: 199px;
    top: 2px;
    width: 801px;
    height: 802px;
    background: var(--card);
    overflow: hidden;
    box-shadow: 0 0 4px rgba(0,0,0,0.25);
  }
  .post__backdrop {
    position: absolute;
    left: 0; top: 208px;
    width: 801px; height: 594px;
    background:
      radial-gradient(ellipse 30% 45% at 20% 35%, var(--photo-mid), transparent 70%),
      radial-gradient(ellipse 28% 45% at 82% 30%, var(--photo-mid), transparent 70%),
      radial-gradient(ellipse 40% 50% at 50% 75%, #e3e3e3, transparent 70%),
      var(--photo-light);
  }
  .post__band {
    position: absolute;
    left: 0; top: 0;
    width: 801px; height: 208px;
    background: var(--navy);
  }
  .candidate-photo {
    position: absolute;
    left: 241px; top: 47px;
    width: 306px; height: 306px;
    border-radius: 50%;
    border: 9px solid var(--white);
    background: radial-gradient(circle at 50% 35%, #c9b3a2 0 18%, #e9e9e9 19% 55%, #3a3a3a 56%);
    box-shadow: 0 4px 10px rgba(0,0,0,0.25);
  }
  .headline {
    position: absolute;
    left: 0; width: 801px;
    text-align: center;
    color: var(--navy-deep);
  }
  .headline--title { top: 379px; font-size: 32px; font-weight: 700; }
  .headline--sub { top: 418px; font-size: 27px; font-weight: 400; }
  .intro {
    position: absolute;
    left: 150px; top: 460px;
    width: 501px;
    text-align: center;
    font-size: 15px;
    line-height: 20px;
    color: var(--text-dark);
  }
  .feature {
    position: absolute;
    top: 540px;
    width: 230px;
    text-align: center;
  }
  .feature--one { left: 34px; }
  .feature--two { left: 285px; }
  .feature--three { left: 538px; }
  .feature__icon { display: block; margin: 0 auto; width: 70px; height: 70px; }
  .feature__title {
    margin-top: 11px;
    font-size: 18px;
    font-weight: 700;
    color: var(--text-grey);
  }
  .feature__text {
    margin-top: 9px;
    font-size: 12.5px;
    line-height: 17px;
    color: var(--text-grey);
  }
  .divider {
    position: absolute;
    top: 566px;
    width: 2px; height: 107px;
    background: linear-gradient(transparent, var(--divider) 30%, var(--divider) 70%, transparent);
  }
  .divider--left { left: 272px; }
  .divider--right { left: 532px; }
  .brand {
    position: absolute;
    left: 52px; top: 733px;
    display: flex;
    align-items: center;
    gap: 8px;
    font-size: 27px;
    font-weight: 700;
    color: var(--navy);
  }
  .brand__mark { width: 16px; height: 16px; background: var(--navy); }
  .cta {
    position: absolute;
    left: 572px; top: 721px;
    width: 193px; height: 51px;
    border-radius: 26px;
    background: linear-gradient(var(--button-top), var(--button-bottom));
    box-shadow: 0 2px 4px rgba(0,0,0,0.3);
    display: flex;
    align-items: center;
    padding-left: 24px;
    color: var(--white);
    font-size: 20px;
    font-weight: 400;
    text-decoration: none;
  }
  .cta__arrow {
    position: absolute;
    right: 8px; top: 8px;
    width: 35px; height: 35px;
  }
</style>
</head>
<body>
  <main class="post">
    <div class="post__backdrop" role="img" aria-label="Faded black and white photo of a team of business people"></div>
    <div class="post__band"></div>
    <div class="candidate-photo" role="img" aria-label="Portrait of the featured candidate in a business suit"></div>

    <h1 class="headline headline--title">Lorem Ipsum</h1>
    <h2 class="headline headline--sub">consectetuer adipiscing</h2>
    <p class="intro">Lorem ipsum dolor sit amet, consectetuer adipiscing elit. Aenean commodo ligula eget dolor. Aenean massa.</p>

    <section class="feature feature--one">
      <svg class="feature__icon" viewBox="0 0 70 70" aria-hidden="true">
        <circle cx="35" cy="35" r="35" fill="var(--navy)"/>
        <rect x="16" y="32" width="8" height="20" rx="2" fill="var(--white)"/>
        <path d="M27 32 L34 20 Q36 15 39 18 Q40 22 38 30 L50 30 Q54 31 53 35 L50 49 Q49 52 46 52 L27 52 Z" fill="var(--white)"/>
      </svg>
      <h3 class="feature__title">Consectetuer</h3>
      <p class="feature__text">Nullam dictum felis eu pede mollis pretium. Integer tincidunt.</p>
    </section>
    <div class="divider divider--left"></div>

    <section class="feature feature--two">
      <svg class="feature__icon" viewBox="0 0 70 70" aria-hidden="true">
        <circle cx="35" cy="35" r="35" fill="var(--navy)"/>
        <circle cx="30" cy="29" r="12" fill="none" stroke="var(--white)" stroke-width="4"/>
        <line x1="39" y1="38" x2="51" y2="50" stroke="var(--white)" stroke-width="7" stroke-linecap="round"/>
      </svg>
      <h3 class="feature__title">Ullamcorper</h3>
      <p class="feature__text">Cras dapibus. Vivamus elementum semper nisi. Aenean vulputate</p>
    </section>
    <div class="divider divider--right"></div>

    <section class="feature feature--three">
      <svg class="feature__icon" viewBox="0 0 70 70" aria-hidden="true">
        <circle cx="35" cy="35" r="35" fill="var(--navy)"/>
        <path d="M33 19 A17 17 0 1 0 51 37 L33 37 Z" fill="var(--white)"/>
        <path d="M37 15 A17 17 0 0 1 55 33 L37 33 Z" fill="none" stroke="var(--white)" stroke-width="3"/>
      </svg>
      <h3 class="feature__title">Pulvinar</h3>
      <p class="feature__text">Curabitur ullacorper ultricies. Nam eget dui. Etiam rhoncus.</p>
    </section>

    <div class="brand"><span class="brand__mark"></span>BRAMO Recruitment</div>

    <a class="cta" href="#">CLICK HERE
      <svg class="cta__arrow" viewBox="0 0 35 35" aria-hidden="true">
        <circle cx="17.5" cy="17.5" r="17" fill="var(--navy-deep)"/>
        <path d="M11 10 L26 17.5 L11 25 L14 17.5 Z" fill="var(--white)"/>
      </svg>
    </a>
  </main>
</body>
</html>
```